Medical Billing Company Needs a Business Card Design

We need a business card design for a Florida based medical billing company called 'Lorrimer Tallbrook Services'. We specialize in providing revenue cycle management services to physician and therapist offices (we're basically their back-office processing partner for providing billing software, claims submissions, A/R follow-up and patient statements & collections. Our logo is red and blue-ish, so make sure that whatever other elements are used will match appropriately. Our current business card design has a too small font size. I'd like to project an image that shows we are modern & reliable. On a side note, I'm planning on using VUX for printing these cards.

Target Market(s)

Office managers, physicians, therapists

Industry/Entity Type

Printing

Requirements
Must have
• Logo
Name of Employee
Phone
Fax
E-mail
Website

```html
<!DOCTYPE html>
<html lang="en">
<head>
<meta charset="utf-8">
<title>Lorrimer Tallbrook Services – Business Card</title>
<link rel="stylesheet" href="https://fonts.googleapis.com/css2?family=Open+Sans:wght@400;600;700&display=swap">
<style>
  :root {
    --page-bg: #e9e9ee;
    --brand-purple: #3b2386;
    --brand-purple-light: #5a4497;
    --brand-purple-dark: #24106b;
    --brand-red: #a3161c;
    --ink: #3a3a3a;
    --paper: #ffffff;
  }
  * { box-sizing: border-box; margin: 0; padding: 0; }
  html, body {
    width: 1200px; height: 987px; overflow: hidden;
    background: var(--page-bg);
    font-family: "Open Sans", Arial, sans-serif;
  }
  .sheet {
    width: 1200px; height: 987px;
    display: flex; flex-direction: column; align-items: center; justify-content: center;
    gap: 60px;
  }
  .card {
    position: relative;
    width: 700px; height: 400px;
    border-radius: 34px;
    overflow: hidden;
    box-shadow: 0 10px 28px rgba(40, 30, 80, 0.18);
  }
  /* Front */
  .card-front { background: var(--paper); }
  .card-front .wave { position: absolute; inset: 0; width: 100%; height: 100%; }
  .brand-name {
    position: absolute; top: 44px; right: 50px;
    display: flex; align-items: center; gap: 12px;
    color: var(--brand-purple);
    font-size: 30px; font-weight: 400; letter-spacing: 1.5px;
    text-transform: uppercase;
  }
  .brand-square { width: 16px; height: 16px; background: var(--brand-red); }
  .holder { position: absolute; top: 100px; left: 54px; }
  .holder-name { font-size: 23px; font-weight: 700; color: var(--brand-purple); }
  .holder-title { font-size: 19px; font-weight: 400; color: var(--brand-red); }
  .contact-list { list-style: none; margin-top: 12px; }
  .contact-list li {
    display: flex; align-items: center; gap: 10px;
    font-size: 17px; color: var(--ink); line-height: 28px;
  }
  .contact-list svg { width: 16px; height: 16px; fill: var(--brand-purple); flex: none; }
  .address {
    position: absolute; right: 40px; bottom: 14px;
    text-align: right; color: var(--paper);
    font-size: 18px; line-height: 25px; font-style: normal;
  }
  /* Back */
  .card-back {
    background: linear-gradient(135deg, var(--brand-purple-light) 0%, var(--brand-purple) 50%, var(--brand-purple-dark) 100%);
    color: var(--paper);
  }
  .back-brand {
    position: absolute; top: 140px; left: 0; right: 0;
    display: flex; align-items: center; justify-content: center; gap: 16px;
    font-size: 36px; font-weight: 400; letter-spacing: 2px; text-transform: uppercase;
  }
  .back-square { width: 20px; height: 20px; border: 2px solid var(--paper); }
  .back-web {
    position: absolute; bottom: 110px; left: 0; right: 0; text-align: center;
    font-size: 19px; letter-spacing: 4px;
  }
</style>
</head>
<body>
<main class="sheet">
  <section class="card card-front">
    <svg class="wave" viewBox="0 0 700 400" preserveAspectRatio="none" aria-hidden="true">
      <path d="M0,272 C60,328 200,320 350,310 C500,300 620,294 700,288 L700,400 L0,400 Z" fill="var(--brand-purple)"/>
      <path d="M0,287 C60,343 200,335 350,325 C500,315 620,309 700,303" fill="none" stroke="var(--brand-red)" stroke-width="6"/>
    </svg>

    <div class="brand-name"><span class="brand-square"></span>Lorrimer Tallbrook</div>

    <div class="holder">
      <p><span class="holder-name">Your Name,</span> <span class="holder-title">Title</span></p>
      <ul class="contact-list">
        <li><svg viewBox="0 0 16 16"><path d="M4 1l3 3-2 2c1 2 3 4 5 5l2-2 3 3-2 3C7 15 1 9 1 3z"/></svg>123-456-0789</li>
        <li><svg viewBox="0 0 16 16"><path d="M4 0h8v16H4zM5.5 2v10h5V2z"/></svg>123-456-0789</li>
        <li><svg viewBox="0 0 16 16"><path d="M1 3h14v10H1zM2 4l6 5 6-5z"/></svg>info@lorrimertallbrook.com</li>
        <li><svg viewBox="0 0 16 16"><path d="M8 1a7 7 0 1 0 0 14A7 7 0 0 0 8 1zm0 1.5c1 1.2 1.6 3 1.7 5H6.3C6.4 5.5 7 3.7 8 2.5zM2.6 7.5h2.2c.1-1.8.5-3.4 1.2-4.5A5.5 5.5 0 0 0 2.6 7.5zm0 1A5.5 5.5 0 0 0 6 13c-.7-1.1-1.1-2.7-1.2-4.5zm3.7 0h3.4c-.1 2-.7 3.8-1.7 5-1-1.2-1.6-3-1.7-5zm4.9 0c-.1 1.8-.5 3.4-1.2 4.5a5.5 5.5 0 0 0 3.4-4.5zm0-1h2.2A5.5 5.5 0 0 0 10 3c.7 1.1 1.1 2.7 1.2 4.5z"/></svg>www.lorrimertallbrook.com</li>
      </ul>
    </div>

    <address class="address">
      Street Name, City Name<br>State Zip Code
    </address>
  </section>

  <section class="card card-back">
    <div class="back-brand"><span class="back-square"></span>Lorrimer Tallbrook</div>
    <p class="back-web">www.lorrimertallbrook.com</p>
  </section>
</main>
</body>
</html>
```